Flyer Design Project

We need a flyer for a monthly event that we will be having. The flyer needs to be editable in either adobe illustrator or photoshop so that we can change the details such as the date if needed... Preferable in vector art.

Name of Event : Sandalmania

Price of Tickets: $15 Tickets- Entry fee ensures a pair of thongs upon leaving, drink specials all night and priority entry.

WHEN- FEB 20th
WHERE- Velvet Lantern
DJ: Tessa Quill
web: www.velvetlanternbar.com.au
ph: 9341 5067

Drink specials from 7-9pm
$3 Pots
$4 basics
$4 brellos

$1 pizza from 8pm-10pm

FREE PAIR OF THONGS ON DEPARTURE

Drink specials continue throughout the night

Open 7pm-3am
Updates

Hi there,

Just to be clear, a pair of thongs isĀ referringĀ to flip flops or sandals (not underwear)... thanks

Target Market(s)

University Students 18-24 years old

Industry/Entity Type

Apartment

Requirements
Must have
• must have our logo

```html
<!DOCTYPE html>
<html lang="en">
<head>
<meta charset="utf-8">
<title>Sandalmania – Velvet Lantern</title>
<link href="https://fonts.googleapis.com/css2?family=Bebas+Neue&family=Oswald:wght@400;500;700&display=swap" rel="stylesheet">
<style>
  :root {
    --backdrop: #e9e9e9;
    --ink: #0d0d0d;
    --yellow: #f5c400;
    --gold: #e3b320;
    --gold-deep: #b8860b;
    --orange: #c8731a;
    --cyan: #1fb8d6;
    --green: #5ff03a;
    --white: #ffffff;
  }
  * { margin: 0; padding: 0; box-sizing: border-box; }
  html, body { width: 1200px; height: 1131px; overflow: hidden; background: var(--backdrop); }
  .flyer {
    position: absolute; left: 213px; top: 30px; width: 773px; height: 1071px;
    background:
      repeating-linear-gradient(90deg, rgba(255,255,255,0.025) 0 2px, transparent 2px 6px),
      var(--ink);
    overflow: hidden;
    font-family: "Oswald", sans-serif;
    color: var(--white);
    box-shadow: 0 10px 30px rgba(0,0,0,0.25);
  }
  .web-band {
    position: absolute; left: 0; top: 0; width: 100%; height: 43px;
    background: repeating-linear-gradient(90deg, var(--yellow) 0 3px, #e2b400 3px 5px);
    color: var(--ink); font-weight: 700; font-size: 22px; letter-spacing: 1px;
    display: flex; align-items: center; justify-content: center; text-transform: uppercase;
  }
  .venue-name {
    position: absolute; left: 24px; top: 66px;
    font-weight: 700; font-size: 84px; line-height: 1; color: var(--white);
    letter-spacing: -1px; text-transform: lowercase;
  }
  .thongs-photo {
    position: absolute; left: 590px; top: 168px; width: 183px; height: 112px;
    background: linear-gradient(160deg, #e85a8f 0%, #3ab0d8 35%, #6cd13e 60%, #f2d12c 100%);
    border-radius: 40px 0 0 40px;
  }
  .giveaway {
    position: absolute; left: 38px; top: 226px;
    color: var(--yellow); font-weight: 700; font-size: 27px; letter-spacing: 0.5px;
  }
  .event-title {
    position: absolute; left: 34px; top: 292px;
    font-family: "Bebas Neue", sans-serif; font-weight: 400; font-size: 122px; line-height: 1; letter-spacing: 2px;
    color: var(--white);
    text-shadow: 3px 3px 0 var(--ink), 6px 6px 0 var(--orange);
  }
  .date-tag {
    position: absolute; left: 29px; top: 468px; width: 340px; height: 52px;
    background: var(--green); color: var(--ink);
    font-weight: 700; font-size: 34px; line-height: 52px; padding-left: 14px;
  }
  .backdrop-shapes { position: absolute; left: 0; top: 0; }
  .ticket-badge {
    position: absolute; left: 447px; top: 422px; width: 304px; height: 304px;
    border-radius: 50%; background: var(--gold);
    text-align: center;
  }
  .ticket-badge::before {
    content: ""; position: absolute; inset: 11px; border-radius: 50%;
    border: 4px dotted var(--ink);
  }
  .crown { position: absolute; left: 129px; top: 36px; }
  .ticket-price {
    position: absolute; left: 0; right: 0; top: 92px;
    font-weight: 700; font-size: 42px; line-height: 1; color: var(--white);
    text-shadow: 2px 2px 0 var(--gold-deep), 3px 3px 0 var(--ink);
  }
  .ticket-label {
    position: absolute; left: 0; right: 0; top: 144px;
    font-weight: 500; font-size: 32px; line-height: 1; color: var(--ink); letter-spacing: 2px;
  }
  .ticket-note {
    position: absolute; left: 52px; right: 52px; top: 188px;
    font-weight: 500; font-size: 17px; line-height: 1.15; color: var(--ink); letter-spacing: 1px;
    border-top: 3px dotted var(--ink); padding-top: 7px;
  }
  .guest-photo {
    position: absolute; left: 5px; top: 640px; width: 200px; height: 412px;
    background: linear-gradient(180deg, #7a4a2c 0%, #c98a62 30%, #8e4aa0 60%, #3fae3a 100%);
    border-radius: 90px 90px 0 0;
  }
  .thongs-row {
    position: absolute; left: 300px; top: 1010px; width: 440px; height: 50px;
    background: linear-gradient(90deg, #c5306a 0%, #c5306a 20%, transparent 20%, transparent 40%, #f2c12c 40%, #f2c12c 55%, transparent 55%, transparent 70%, #f2c12c 70%, #f2c12c 85%, transparent 85%);
    border-radius: 0 0 20px 20px;
  }
  .info-panel {
    position: absolute; left: 142px; top: 802px; width: 618px; height: 240px;
    background: rgba(20,20,20,0.92);
    display: flex; padding: 14px 0 0 14px;
  }
  .info-col { width: 315px; }
  .info-col + .info-col { border-left: 2px dotted var(--white); padding-left: 18px; width: 290px; }
  .info-heading { font-weight: 500; font-size: 36px; line-height: 1.1; }
  .dotted-rule { border-bottom: 3px dotted var(--white); margin: 4px 20px 8px 0; }
  .info-line { font-size: 22px; line-height: 1.55; font-weight: 400; }
  .info-line.big { font-size: 34px; line-height: 1.2; font-weight: 500; }
  .specials { display: flex; gap: 24px; }
  .base-band { position: absolute; left: 0; bottom: 0; width: 100%; height: 12px; background: var(--yellow); }
</style>
</head>
<body>
<main class="flyer">
  <svg class="backdrop-shapes" width="773" height="1071" viewBox="0 0 773 1071" aria-hidden="true">
    <defs>
      <pattern id="yellowRules" width="20" height="10" patternUnits="userSpaceOnUse">
        <rect x="0" y="0" width="3" height="10" fill="#f5c400"/>
      </pattern>
    </defs>
    <rect x="0" y="725" width="773" height="335" fill="url(#yellowRules)" opacity="0.9"/>
    <polygon points="0,653 773,571 773,648 0,742" fill="#1fb8d6"/>
    <polygon points="0,742 773,648 773,668 0,770" fill="#0d0d0d"/>
  </svg>

  <div class="web-band">www.velvetlanternbar.com.au</div>
  <div class="venue-name">Velvet Lantern</div>

  <div class="thongs-photo" role="img" aria-label="Stack of colourful flip-flop thongs"></div>

  <div class="giveaway">FREE PAIR OF THONGS ON DEPARTURE</div>
  <h1 class="event-title">SANDALMANIA</h1>
  <div class="date-tag">★ FEBRUARY 20TH</div>

  <div class="ticket-badge">
    <svg class="crown" width="46" height="38" viewBox="0 0 50 40" aria-hidden="true">
      <polygon points="4,32 2,8 15,20 25,2 35,20 48,8 46,32" fill="#0d0d0d"/>
      <rect x="4" y="34" width="42" height="5" fill="#0d0d0d"/>
    </svg>
    <div class="ticket-price">$15 TICKETS</div>
    <div class="ticket-label">ENTRY FEE</div>
    <div class="ticket-note">ENSURES A PAIR OF THONGS UPON LEAVING</div>
  </div>

  <div class="guest-photo" role="img" aria-label="Young woman holding up a pair of thongs"></div>
  <div class="thongs-row" role="img" aria-label="Row of colourful thongs along the bottom edge"></div>

  <section class="info-panel">
    <div class="info-col">
      <div class="info-heading">DJ: TESSA QUILL</div>
      <div class="dotted-rule"></div>
      <div class="info-line">DRINK SPECIALS FROM 7-9PM</div>
      <div class="specials">
        <div class="info-line">$3 POTS</div>
        <div class="info-line">$1 PIZZA 8PM-10PM</div>
      </div>
      <div class="info-line">$4 BASICS</div>
      <div class="info-line">$4 BRELLOS</div>
    </div>
    <div class="info-col">
      <div class="info-line big">OPEN 7PM-3AM</div>
      <div class="info-line big">VELVET LANTERN</div>
      <div class="info-line big">PH: 9341 5067</div>
      <div class="info-line">DRINK SPECIALS ALL NIGHT</div>
      <div class="info-line">AND PRIORITY ENTRY</div>
    </div>
  </section>

  <div class="base-band"></div>
</main>
</body>
</html>
```